Redesign of TaskHarbor.com website

Our website was initially developed 6+ years ago and has been maintained by several different designers. As a result, it is overly complex, inconsistent format/layout and the content is not well structured/easy to navigate

We need the site redeveloped with a more modern look and feel, simpler content structure and ability to implement new/improved tools, such as: Dynamic Forms, Sales Funnels, Landing Pages, improved metadata of our pages and posts, improved SEO/Page ranking, etc.

We currently use DealRiver CRM, Steady Reach for marketing automation and GridPilot forms. We are investigating Floxen for workflow integration which could extend to our website.

Our current website is developed in WordPress, ideally we will stick with this platform, but we’re happy to consider other CMS' if strongly recommended. We may decide to remove/consolidate some of the pages and/or content as part of this re-design.

We don't want to rebrand (ie change corporate logo, colours scheme etc) as part of this website redevelopment and it is critical that we don't lose our current Page Ranking, SEO rankings, backlink benefits, etc as part of this redevelopment.

Sites we like the feel/design of are: boardwiley.com, tallypoint.com and rankgrove.com

Target Market(s)

Corporate, Enterprise and Government B2B clients.

Coding

Coded - Design and coding required

Number of Pages Required

5+ page

Font styles to use
Sans Serif

Colors
ffffff
ec1f27

Requirements
Must have
• Must retain the majority of content on our existing website (although we may re-write some of it as part of this redesign process).
Nice to have
• See above "Project Description"
Should not have

```html
<!DOCTYPE html>
<html lang="en">
<head>
<meta charset="utf-8">
<title>TaskHarbor – Your Trusted Advisor</title>
<link href="https://fonts.googleapis.com/css2?family=Roboto:ital,wght@0,400;0,500;0,700;1,400&display=swap" rel="stylesheet">
<style>
:root{
  --red:#ec1f27;
  --white:#ffffff;
  --ink:#1b1b1b;
  --grey:#666;
  --muted:#7a7a7a;
  --soft:#f4f7fd;
  --panel:#f3f3f3;
  --footer:#222222;
}
*{box-sizing:border-box;margin:0;padding:0}
html,body{width:1200px;height:3189px;overflow:hidden}
body{font-family:'Roboto',sans-serif;color:var(--ink);background:var(--white);position:relative}
.abs{position:absolute}
a{color:inherit;text-decoration:none}

/* header */
.site-header{position:absolute;left:0;top:0;width:1200px;height:106px;background:var(--white)}
.brand{position:absolute;display:flex;align-items:center;gap:10px}
.brand-dot{width:26px;height:26px;border-radius:50%;background:var(--red)}
.brand-name{font-size:34px;font-weight:400;color:var(--red);line-height:1}
.brand-tag{position:absolute;font-size:11px;color:#888}
.social{position:absolute;width:28px;height:28px;border:1.5px solid #555;border-radius:50%}
.call-label{left:952px;top:18px;font-size:13px;color:#444}
.call-number{left:952px;top:38px;font-size:18px;font-weight:700}
.nav{position:absolute;top:79px;font-size:15px;font-weight:500;color:#222}
.nav.active{color:var(--red)}

/* hero */
.hero{position:absolute;left:0;top:106px;width:1200px;height:602px;
  background:linear-gradient(180deg,#3e5570 0%,#5a6d86 30%,#3a3a45 55%,#2a2418 75%,#181a22 100%)}
.hero-title{position:absolute;left:0;width:1200px;top:192px;text-align:center;font-size:56px;font-weight:700;color:var(--white)}
.hero-text{position:absolute;left:0;width:1200px;top:274px;text-align:center;font-size:17px;font-weight:500;color:var(--white);line-height:26px}
.btn{display:inline-flex;align-items:center;gap:8px;background:var(--red);color:var(--white);font-weight:700;border-radius:30px;text-transform:uppercase}
.hero-btn{position:absolute;left:494px;top:350px;height:48px;padding:0 38px;font-size:16px}
.hero-arrow{position:absolute;top:282px;width:36px;height:36px;border:2px solid var(--white);border-radius:50%}

/* services */
.section-title{position:absolute;left:0;width:1200px;text-align:center;font-size:40px;font-weight:700}
.section-title .accent{color:var(--red)}
.section-title .quiet{color:#777}
.service-card{position:absolute;width:270px;background:var(--soft);text-align:center}
.service-card.featured{background:var(--white);box-shadow:0 4px 18px rgba(0,0,0,.12)}
.service-card svg{display:block;margin:0 auto}
.service-card h3{font-size:17px;font-weight:700;margin:14px 0 18px}
.service-card p{font-size:14px;color:var(--grey);line-height:22px}
.learn{display:inline-flex;align-items:center;gap:6px;color:var(--red);font-weight:700;font-size:14px;margin-top:14px}

/* about */
.about{position:absolute;left:0;top:1284px;width:1200px;height:481px;background:var(--panel)}
.about h2{position:absolute;left:110px;top:54px;font-size:33px;font-weight:500;color:#777;line-height:38px}
.about h2 b{color:var(--red);font-weight:700}
.about .lead{position:absolute;left:111px;top:138px;font-size:16px;font-weight:500}
.about .body{position:absolute;left:111px;top:180px;width:470px;font-size:14px;color:var(--grey);line-height:22px}
.about .body p{margin-bottom:7px}
.about-btn{position:absolute;left:111px;top:370px;height:46px;padding:0 36px;font-size:14px}
.about-photo{position:absolute;left:661px;top:0;width:539px;height:481px;background:linear-gradient(135deg,#d8dde4,#a9b3bf 45%,#6f6a62 80%,#3b3d42)}

/* testimonial */
.testimonial{position:absolute;left:0;top:1765px;width:1200px;height:340px;background:var(--red);color:var(--white)}
.testimonial h2{position:absolute;left:322px;top:60px;font-size:40px;font-weight:700}
.avatar{position:absolute;left:188px;top:128px;width:92px;height:92px;transform:rotate(45deg);background:linear-gradient(135deg,#f1d2c2,#b7774f);border:3px solid #e6e6e6}
.quote{position:absolute;left:323px;top:132px;width:680px;font-size:15px;font-style:italic;line-height:27px}
.quote-name{position:absolute;left:323px;top:240px;font-size:17px;font-weight:700}
.quote-role{position:absolute;left:323px;top:265px;font-size:12px}

/* news */
.news-card{position:absolute;background:var(--white);box-shadow:0 2px 10px rgba(0,0,0,.12)}
.news-feature{left:134px;top:2262px;width:443px;height:450px;text-align:center}
.news-feature .thumb{position:absolute;left:7px;top:8px;width:429px;height:291px;background:linear-gradient(135deg,#cfd2d3,#8d9194 55%,#5f6264)}
.news-feature h3{position:absolute;left:0;width:443px;top:326px;font-size:16px;font-weight:500}
.meta{font-size:13px;color:var(--red);display:flex;align-items:center;gap:6px}
.news-feature .meta{position:absolute;left:0;width:443px;top:356px;justify-content:center}
.news-feature .excerpt{position:absolute;left:40px;width:363px;top:388px;font-size:14px;color:var(--grey);line-height:22px}
.news-item{left:614px;width:444px;height:136px}
.news-item .thumb{position:absolute;left:8px;top:8px;width:152px;height:120px}
.news-item h3{position:absolute;left:177px;top:18px;font-size:15px;font-weight:500}
.news-item .meta{position:absolute;left:177px;top:44px}
.news-item .excerpt{position:absolute;left:177px;top:74px;width:255px;font-size:13.5px;color:var(--grey);line-height:20px}

/* footer */
.site-footer{position:absolute;left:0;top:2823px;width:1200px;height:366px;background:var(--footer);color:var(--white)}
.site-footer .brand-name{font-size:36px}
.foot-social{position:absolute;top:174px;width:38px;height:38px;border:1.5px solid var(--white);border-radius:50%}
.foot-head{position:absolute;top:66px;font-size:16px;font-weight:700}
.foot-links{position:absolute;top:108px;font-size:13px;color:#ddd;list-style:none;line-height:26px}
.contact-row{position:absolute;left:853px;display:flex;gap:12px;font-size:13px;color:#ddd}
.contact-row b{display:block;font-size:11px;color:var(--white);font-weight:700;margin-bottom:2px}
.foot-rule{position:absolute;left:111px;top:292px;width:978px;height:1px;background:#666}
.to-top{position:absolute;left:1105px;top:274px;width:36px;height:36px;border-radius:50%;background:var(--red)}
.copyright{position:absolute;left:0;width:1200px;top:318px;text-align:center;font-size:14px;color:#ddd}
</style>
</head>
<body>

<header class="site-header">
  <div class="brand" style="left:111px;top:32px">
    <span class="brand-dot"></span><span class="brand-name">taskharbor</span>
  </div>
  <span class="brand-tag" style="left:232px;top:64px">your trusted advisor</span>
  <span class="social" style="left:720px;top:27px" aria-label="Social link"></span>
  <span class="social" style="left:759px;top:27px" aria-label="Social link"></span>
  <span class="social" style="left:797px;top:27px" aria-label="Social link"></span>
  <span class="social" style="left:836px;top:27px" aria-label="Social link"></span>
  <svg class="abs" style="left:900px;top:28px" width="26" height="26" viewBox="0 0 24 24" fill="none" stroke="#666" stroke-width="1.6"><path d="M5 3h4l2 5-2.5 1.5a11 11 0 0 0 6 6L16 13l5 2v4a2 2 0 0 1-2 2A16 16 0 0 1 3 5a2 2 0 0 1 2-2z"/></svg>
  <div class="abs" style="left:942px;top:22px;width:1px;height:34px;background:#bbb"></div>
  <span class="abs call-label">Call Now</span>
  <span class="abs call-number">1(877) 555.0142</span>
  <span class="abs" style="left:549px;top:52px;width:14px;height:14px;border-radius:50%;background:var(--red)"></span>
  <a class="nav active" style="left:536px">Home</a>
  <a class="nav" style="left:604px">Services</a>
  <a class="nav" style="left:690px">About</a>
  <a class="nav" style="left:759px">Clients</a>
  <a class="nav" style="left:833px">Resources</a>
  <a class="nav" style="left:934px">Blog</a>
  <a class="nav" style="left:991px">Contact</a>
  <svg class="abs" style="left:1073px;top:82px" width="15" height="15" viewBox="0 0 16 16" fill="none" stroke="#222" stroke-width="2.2"><circle cx="6.5" cy="6.5" r="5"/><path d="M10.5 10.5L15 15"/></svg>
</header>

<section class="hero" role="img" aria-label="City harbour skyline at dusk with lights reflected on the water">
  <h1 class="hero-title">TaskHarbor</h1>
  <p class="hero-text">TaskHarbor provides an ongoing management and maintenance<br>service to ensure that plan documentation</p>
  <a class="btn hero-btn">Get Started
    <svg width="16" height="16" viewBox="0 0 16 16"><circle cx="8" cy="8" r="8" fill="#fff"/><path d="M6.5 4.5L10 8l-3.5 3.5" stroke="#ec1f27" stroke-width="2" fill="none"/></svg></a>
  <span class="hero-arrow" style="left:34px"><svg width="32" height="32" viewBox="0 0 32 32"><path d="M18 10l-6 6 6 6" stroke="#fff" stroke-width="2" fill="none"/></svg></span>
  <span class="hero-arrow" style="left:1126px"><svg width="32" height="32" viewBox="0 0 32 32"><path d="M14 10l6 6-6 6" stroke="#fff" stroke-width="2" fill="none"/></svg></span>
</section>

<h2 class="section-title" style="top:786px"><span class="accent">Our</span> <span class="quiet">Services</span></h2>

<article class="service-card" style="left:31px;top:892px;height:272px;padding-top:26px">
  <svg width="48" height="48" viewBox="0 0 48 48" fill="none" stroke="#333" stroke-width="1.6"><circle cx="16" cy="22" r="6"/><circle cx="32" cy="22" r="6"/><path d="M5 44c0-7 5-12 11-12s11 5 11 12M21 44c0-7 5-12 11-12s11 5 11 12"/><rect x="4" y="3" width="14" height="9" rx="2" stroke="#ec1f27"/><rect x="30" y="3" width="14" height="9" rx="2" stroke="#ec1f27"/></svg>
  <h3>Resilience &amp; Continuity</h3>
  <p>Business Continuity Management<br>Disaster Recovery Planning<br>Crisis Management<br>Emergency Management Planning</p>
  <a class="learn">LEARN MORE <svg width="13" height="13" viewBox="0 0 16 16"><circle cx="8" cy="8" r="8" fill="#ec1f27"/><path d="M6.5 4.5L10 8l-3.5 3.5" stroke="#fff" stroke-width="2" fill="none"/></svg></a>
</article>
<article class="service-card featured" style="left:320px;top:870px;height:316px;padding-top:46px">
  <svg width="48" height="48" viewBox="0 0 48 48" fill="none" stroke="#333" stroke-width="1.6"><path d="M24 3l18 7v12c0 12-8 20-18 24C14 42 6 34 6 22V10z"/><rect x="17" y="22" width="14" height="11" rx="1.5" stroke="#ec1f27"/><path d="M20 22v-4a4 4 0 0 1 8 0v4" stroke="#ec1f27"/></svg>
  <h3>Security Management</h3>
  <p>Business Continuity Management<br>Disaster Recovery Planning<br>Crisis Management<br>Emergency Management Planning</p>
  <a class="learn">LEARN MORE <svg width="13" height="13" viewBox="0 0 16 16"><circle cx="8" cy="8" r="8" fill="#ec1f27"/><path d="M6.5 4.5L10 8l-3.5 3.5" stroke="#fff" stroke-width="2" fill="none"/></svg></a>
</article>
<article class="service-card" style="left:609px;top:892px;height:272px;padding-top:26px">
  <svg width="48" height="48" viewBox="0 0 48 48" fill="none" stroke="#333" stroke-width="1.6"><rect x="3" y="14" width="32" height="22" rx="2"/><path d="M13 44h12M19 36v8"/><circle cx="34" cy="14" r="9" stroke="#ec1f27"/><circle cx="34" cy="14" r="3" stroke="#ec1f27"/></svg>
  <h3>IT Services &amp; Solutions</h3>
  <p>Business Continuity Management<br>Disaster Recovery Planning<br>Crisis Management<br>Emergency Management Planning</p>
  <a class="learn">LEARN MORE <svg width="13" height="13" viewBox="0 0 16 16"><circle cx="8" cy="8" r="8" fill="#ec1f27"/><path d="M6.5 4.5L10 8l-3.5 3.5" stroke="#fff" stroke-width="2" fill="none"/></svg></a>
</article>
<article class="service-card" style="left:898px;top:892px;height:272px;padding-top:26px">
  <svg width="48" height="48" viewBox="0 0 48 48" fill="none" stroke="#333" stroke-width="1.6"><circle cx="12" cy="14" r="5"/><path d="M4 36c0-6 4-10 8-10s8 4 8 10"/><path d="M26 44V30M32 44V24M38 44V18M44 44V12M22 44h24"/><rect x="30" y="2" width="14" height="8" rx="1.5" stroke="#ec1f27"/><circle cx="12" cy="38" r="4" stroke="#ec1f27"/></svg>
  <h3>Data Governance Services</h3>
  <p>Business Continuity Management<br>Disaster Recovery Planning<br>Crisis Management<br>Emergency Management Planning</p>
  <a class="learn">LEARN MORE <svg width="13" height="13" viewBox="0 0 16 16"><circle cx="8" cy="8" r="8" fill="#ec1f27"/><path d="M6.5 4.5L10 8l-3.5 3.5" stroke="#fff" stroke-width="2" fill="none"/></svg></a>
</article>

<section class="about">
  <h2>How To Ensure Your <b>Business<br>Is 100% Safe</b></h2>
  <p class="lead">Your business is only as strong as its weakest link.</p>
  <div class="body">
    <p>As an executive in any business, it is understandable that you want to ensure it is 100% safe, because your business is only as strong as its weakest link.</p>
    <p>You know that if you have a disastrous incident it will cause irreversible damage to your company’s good name, your shareholders, board of directors and industry regulators. It will also cause severe legal ramifications.</p>
  </div>
  <a class="btn about-btn">Read More <svg width="14" height="14" viewBox="0 0 16 16"><circle cx="8" cy="8" r="8" fill="#fff"/><path d="M6.5 4.5L10 8l-3.5 3.5" stroke="#ec1f27" stroke-width="2" fill="none"/></svg></a>
  <div class="about-photo" role="img" aria-label="Team of colleagues discussing documents around an office table"></div>
</section>

<section class="testimonial">
  <h2>What Our Clients Have To Say</h2>
  <svg class="abs" style="left:108px;top:160px" width="28" height="44" viewBox="0 0 28 44"><path d="M22 4L6 22l16 18" stroke="#fff" stroke-width="5" fill="none" opacity=".85"/></svg>
  <svg class="abs" style="left:1064px;top:160px" width="28" height="44" viewBox="0 0 28 44"><path d="M6 4l16 18L6 40" stroke="#fff" stroke-width="5" fill="none" opacity=".85"/></svg>
  <div class="avatar" role="img" aria-label="Client portrait"></div>
  <span class="abs" style="left:284px;top:112px;font-size:44px;font-weight:700;color:#f4a3a6">“</span>
  <p class="quote">“With all due respect, I don’t see TaskHarbor in the classic consultant mould.  I see you far more as ‘hands-on implementation practitioners’, working closely with us to define and implement real solutions to meet our business strategies”</p>
  <span class="abs" style="left:624px;top:186px;font-size:44px;font-weight:700;color:#f4a3a6">”</span>
  <p class="quote-name">Lena Corvell</p>
  <p class="quote-role">Head of Delivery Management</p>
</section>

<h2 class="section-title" style="top:2180px;font-weight:500;font-size:39px">The Latest News &amp; Information</h2>

<article class="news-card news-feature">
  <div class="thumb" role="img" aria-label="Hands being washed with soap under a tap"></div>
  <h3>COVID19 – Business Recovery Phase</h3>
  <div class="meta">▦ 19 August 2020 &nbsp;| &nbsp;◯ TaskHarbor</div>
  <p class="excerpt">The following is a summary of the status updates and actions in preparing for the Recovery Phase</p>
</article>
<article class="news-card news-item" style="top:2262px">
  <div class="thumb" role="img" aria-label="Dark close-up of machine parts" style="background:linear-gradient(135deg,#555,#111)"></div>
  <h3>Decommissioning is Part of Disaster</h3>
  <div class="meta">▦ 3 May 2018 &nbsp;| &nbsp;◯ TaskHarbor</div>
  <p class="excerpt">More moving parts mean more chance of failure. Replace “moving parts”</p>
</article>
<article class="news-card news-item" style="top:2418px">
  <div class="thumb" role="img" aria-label="Hand writing a note about adapting to change" style="background:linear-gradient(135deg,#eeeeee,#c9c9c9)"></div>
  <h3>Adapt or Die – A Darwinian Take on</h3>
  <div class="meta">▦ Dec 20, 2020 &nbsp;| &nbsp;◯ TaskHarbor</div>
  <p class="excerpt">Most businesses experience change constantly. Markets,</p>
</article>
<article class="news-card news-item" style="top:2576px">
  <div class="thumb" role="img" aria-label="Businessperson holding a tablet against a city backdrop" style="background:linear-gradient(135deg,#dfe6ee,#7d8ea3 60%,#2f3e55)"></div>
  <h3>How’s Your User Experience for Your</h3>
  <div class="meta">▦ Dec 19, 2020 &nbsp;| &nbsp;◯ TaskHarbor</div>
  <p class="excerpt">It may sound strange to talk about “touchy-feely” stuff like user</p>
</article>

<footer class="site-footer">
  <div class="brand" style="left:109px;top:80px">
    <span class="brand-dot"></span><span class="brand-name">taskharbor</span>
  </div>
  <span class="brand-tag" style="left:244px;top:117px;color:#ddd">your trusted advisor</span>
  <span class="foot-social" style="left:154px" aria-label="Social link"></span>
  <span class="foot-social" style="left:203px" aria-label="Social link"></span>
  <span class="foot-social" style="left:251px" aria-label="Social link"></span>
  <span class="foot-social" style="left:300px" aria-label="Social link"></span>

  <h4 class="foot-head" style="left:455px">Quick Links</h4>
  <ul class="foot-links" style="left:456px"><li>Home</li><li>Services</li><li>About</li><li>Clients</li><li>Resources</li></ul>
  <h4 class="foot-head" style="left:638px">About Company</h4>
  <ul class="foot-links" style="left:638px"><li>Terms of Use</li><li>Terms &amp; Condition</li><li>News</li><li>Privacy Policy</li><li>FAQ</li></ul>
  <h4 class="foot-head" style="left:853px">Contact Us</h4>
  <div class="contact-row" style="top:104px">
    <svg width="12" height="12" viewBox="0 0 24 24" fill="#ec1f27"><path d="M5 2h5l2 6-3 2a12 12 0 0 0 5 5l2-3 6 2v5a2 2 0 0 1-2 2A18 18 0 0 1 3 4a2 2 0 0 1 2-2z"/></svg>
    <div><b>Phone</b>1300-555-018</div>
  </div>
  <div class="contact-row" style="top:156px">
    <svg width="14" height="12" viewBox="0 0 24 20"><rect width="24" height="18" rx="2" fill="#ec1f27"/><path d="M2 3l10 8 10-8" stroke="#fff" stroke-width="2" fill="none"/></svg>
    <div><b>Email</b>info@taskharbor.com</div>
  </div>
  <div class="contact-row" style="top:206px">
    <svg width="12" height="14" viewBox="0 0 24 28" fill="#ec1f27"><path d="M12 0a10 10 0 0 1 10 10c0 8-10 18-10 18S2 18 2 10A10 10 0 0 1 12 0z"/><circle cx="12" cy="10" r="4" fill="#222"/></svg>
    <div><b>Location</b>48 Harbour Lane Northbank NSW<br>2100 Australia</div>
  </div>
  <div class="foot-rule"></div>
  <span class="to-top"><svg width="36" height="36" viewBox="0 0 36 36"><path d="M13 20l5-5 5 5" stroke="#fff" stroke-width="2.2" fill="none"/></svg></span>
  <p class="copyright">2021 Copyright -  taskharbor  | All Rights Reserved</p>
</footer>

</body>
</html>
```